Website Design for Employee Moral and Happiness Company

Looking for a clean website design that explains our features in a step by step manner so our visitors know exactly what our site does before logging in.

The site is called "Velquo". See logo design and video for a sample of style and an overview of what we do.

Target Market(s)

Business owners that are looking to retain employees.

Number of Pages Required

1 page

```html
<!DOCTYPE html>
<html lang="en">
<head>
<meta charset="utf-8">
<title>Velquo</title>
<link href="https://fonts.googleapis.com/css2?family=Poppins:wght@400;500;600;700&family=Playfair+Display:wght@600&family=Titillium+Web:wght@600&display=swap" rel="stylesheet">
<style>
:root{
  --orange:#e05a1b;
  --orange-dark:#c94c12;
  --ink:#1b1b1b;
  --text:#444;
  --muted:#8a8a8a;
  --white:#fff;
  --footer:#1c1c1c;
  --star:#f2b31c;
}
*{margin:0;padding:0;box-sizing:border-box}
html,body{width:1200px;height:4240px;overflow:hidden}
body{position:relative;font-family:'Poppins',sans-serif;color:var(--ink);background:var(--white)}
.abs{position:absolute}
.btn{position:absolute;display:flex;align-items:center;justify-content:center;border-radius:30px;font-weight:500}
.btn-orange{background:var(--orange);color:var(--white)}
.btn-white{background:var(--white);color:var(--ink)}

/* top bar */
.topbar{left:0;top:0;width:1200px;height:52px;background:var(--orange);color:var(--white);font-size:15px}
.topbar .item{position:absolute;top:15px;display:flex;align-items:center;gap:10px}
.social{position:absolute;top:11px;width:30px;height:30px;border:2px solid var(--white);border-radius:50%}

/* nav */
.nav{left:0;top:52px;width:1200px;height:72px;background:var(--white)}
.logo{position:absolute;font-weight:600;letter-spacing:1px}
.nav .logo{left:110px;top:4px;font-size:48px;color:var(--ink)}
.nav-links{position:absolute;left:364px;top:22px;display:flex;gap:26px;font-size:21px;font-weight:500}
.nav-links .active{color:var(--orange);border-bottom:3px solid var(--orange);padding-bottom:13px}

/* hero */
.hero{left:0;top:124px;width:1200px;height:581px;background:linear-gradient(90deg,#3d3a37 0%,#6b645c 40%,#a79c90 70%,#d8d3cc 100%)}
.hero h1{position:absolute;left:110px;top:110px;color:var(--white);font-weight:400;font-size:52px;line-height:1}
.hero .logo{left:110px;top:165px;font-size:70px;color:var(--white)}
.hero p{position:absolute;left:112px;top:262px;width:440px;color:var(--white);font-size:18px;line-height:26px}
.dot{position:absolute;top:537px;width:16px;height:16px;border-radius:50%;border:2px solid var(--white)}

/* about */
.about-photo{left:118px;top:768px;width:390px;height:390px;border-radius:50%;background:radial-gradient(circle at 40% 40%,#8f7a66,#2d3a55 70%);box-shadow:0 10px 24px rgba(0,0,0,.35)}
.about h2{position:absolute;left:647px;top:790px;font-size:30px;font-weight:600}
.about h3{position:absolute;left:647px;top:846px;font-size:38px;font-weight:600;color:var(--orange)}
.about p{position:absolute;left:645px;top:918px;width:440px;font-size:17px;line-height:35.5px;color:var(--text)}

/* features */
.features{left:0;top:1256px;width:1200px;height:1062px;background:linear-gradient(135deg,#e0601f,#d8561a 50%,#cc4f15)}
.section-title{position:absolute;left:0;width:1200px;text-align:center;font-size:30px;font-weight:700;letter-spacing:1px;color:var(--white)}
.feat h3{position:absolute;color:var(--white);font-size:36px;font-weight:700;line-height:40px}
.feat p{position:absolute;color:var(--white);font-size:18px;line-height:28.5px;text-align:justify}
.frame{position:absolute;border:3px solid var(--white)}
.photo{position:absolute}

/* testimonials */
.testi-title{left:0;top:2372px;width:1200px;text-align:center;font-family:'Titillium Web',sans-serif;font-size:34px;font-weight:600}
.testi-band{left:0;top:2430px;width:1200px;height:220px;overflow:hidden}
.card{position:absolute;top:0;width:520px;text-align:center}
.card .name{font-family:'Playfair Display',serif;color:var(--orange);font-size:18px}
.card .year{font-size:15px;color:var(--text);margin-top:2px}
.card .stars{color:var(--star);font-size:17px;letter-spacing:3px;margin-top:2px}
.card .quote{font-size:14.5px;line-height:24.5px;color:var(--text);margin-top:4px;position:relative;padding:0 6px}
.card.side .quote,.card.side .year{color:var(--muted)}
.qmark{position:absolute;font-family:'Playfair Display',serif;font-size:30px;color:var(--muted)}

/* video */
.video-band{left:0;top:2746px;width:1200px;height:439px;background:var(--orange)}
.video{left:112px;top:2872px;width:976px;height:522px;border-radius:22px;background:linear-gradient(180deg,#1f3550 0%,#2a8a9c 35%,#d9cfc1 62%,#c9bfb0 82%,#2c3a6a 100%);box-shadow:0 8px 20px rgba(0,0,0,.25)}

/* contact */
.contact h2{position:absolute;left:0;top:3460px;width:1200px;text-align:center;color:var(--orange);font-size:30px;font-weight:500}
.contact .lead{position:absolute;left:0;top:3520px;width:1200px;text-align:center;font-size:15px;line-height:22px;font-weight:500}
.field{position:absolute;left:112px;width:426px;border:2px solid #cfcfcf;border-radius:6px;font-size:13px;padding:14px 14px;color:var(--ink)}
.icon{position:absolute;left:580px;width:72px;height:72px;border-radius:50%;background:var(--orange);display:flex;align-items:center;justify-content:center}
.info{position:absolute;left:688px;font-size:19px;line-height:28px;font-weight:500}

/* footer */
.footer{left:0;top:3959px;width:1200px;height:281px;background:var(--footer);color:var(--white)}
.footer .addr{position:absolute;left:112px;top:88px;width:260px;font-size:12.5px;line-height:26px}
.footer .logo{left:458px;top:66px;font-size:60px;color:var(--white)}
.footer .links{position:absolute;left:773px;top:110px;display:flex;gap:20px;font-size:13px}
.footer .copy{position:absolute;left:0;top:222px;width:1200px;text-align:center;font-size:15px;font-weight:500}
</style>
</head>
<body>

<header class="abs topbar">
  <div class="item" style="left:112px">
    <svg width="16" height="12" viewBox="0 0 16 12"><rect x="1" y="1" width="14" height="10" fill="none" stroke="#fff" stroke-width="1.6"/><path d="M1 1l7 6 7-6" fill="none" stroke="#fff" stroke-width="1.6"/></svg>
    info@velquo.com
  </div>
  <div class="item" style="left:355px">
    <svg width="13" height="13" viewBox="0 0 24 24"><path fill="#fff" d="M6.6 10.8a15.1 15.1 0 0 0 6.6 6.6l2.2-2.2c.3-.3.7-.4 1-.2 1.1.4 2.3.6 3.6.6.6 0 1 .4 1 1V20c0 .6-.4 1-1 1A17 17 0 0 1 3 4c0-.6.4-1 1-1h3.5c.6 0 1 .4 1 1 0 1.3.2 2.5.6 3.6.1.3 0 .7-.2 1z"/></svg>
    +1 555 014 2290
  </div>
  <span class="social" style="left:962px"></span>
  <span class="social" style="left:1004px"></span>
  <span class="social" style="left:1046px"></span>
</header>

<nav class="abs nav">
  <div class="logo">Velquo</div>
  <div class="nav-links">
    <span class="active">Home</span><span>About Us</span><span>How Its Work</span><span>Blog</span><span>Contact</span>
  </div>
  <div class="btn btn-orange" style="left:920px;top:14px;width:168px;height:42px;font-size:21px">Login</div>
</nav>

<section class="abs hero" role="img" aria-label="Photo of a smiling businessman in a bright office">
  <h1>WELCOME TO</h1>
  <div class="logo">Velquo</div>
  <p>Lorem ipsum dolor sit amet, consectetur adipiscing elit, sed do eiusmod tempor incididunt ut labore et dolore magna aliqua.</p>
  <div class="btn btn-orange" style="left:110px;top:370px;width:173px;height:46px;font-size:17px">Get Started</div>
  <span class="dot" style="left:565px"></span>
  <span class="dot" style="left:591px;background:var(--orange);border-color:var(--orange)"></span>
  <span class="dot" style="left:617px"></span>
</section>

<section class="about">
  <div class="abs about-photo" role="img" aria-label="Photo of business people shaking hands over a meeting table"></div>
  <h2>About Us</h2>
  <h3>Welcome To Velquo</h3>
  <p>Sed ut perspiciatis unde omnis iste natus error sit voluptatem accusantium doloremque laudantium, totam rem aperiam, eaque ipsa quae ab illo inventore veritatis et quasi architecto beatae vitae dicta sunt explicabo.</p>
  <div class="btn btn-orange" style="left:647px;top:1124px;width:138px;height:42px;font-size:18px">Read More</div>
</section>

<section class="abs features">
  <div class="section-title" style="top:60px">OUR FEATURES</div>
  <div class="feat">
    <h3 style="left:110px;top:160px;width:520px">We champion the bold to achieve the extraordinary</h3>
    <p style="left:114px;top:270px;width:457px">Sed ut perspiciatis unde omnis iste natus error sit voluptatem accusantium doloremque laudantium, totam rem aperiam, eaque ipsa quae ab illo quasi beatae vitae dicta sunt explicabo.</p>
    <div class="btn btn-white" style="left:110px;top:426px;width:171px;height:51px;font-size:18px">Read More</div>
    <div class="frame" style="left:890px;top:115px;width:234px;height:420px"></div>
    <div class="photo" role="img" aria-label="Photo of two colleagues laughing and bumping fists" style="left:681px;top:156px;width:405px;height:339px;background:linear-gradient(135deg,#7c8fa2,#3c4656 60%,#2a2f38)"></div>

    <div class="frame" style="left:61px;top:551px;width:234px;height:420px"></div>
    <div class="photo" role="img" aria-label="Photo of people reviewing a financial statement at a computer" style="left:112px;top:593px;width:405px;height:338px;background:linear-gradient(135deg,#eef1f3,#cdd6dd 55%,#a7b2bc)"></div>
    <h3 style="left:630px;top:604px;width:470px">Product &amp; Experience Innovation</h3>
    <p style="left:632px;top:700px;width:456px">Sed ut perspiciatis unde omnis iste natus error sit voluptatem accusantium doloremque laudantium, totam rem aperiam, eaque ipsa quae ab illo quasi beatae vitae dicta sunt explicabo.</p>
    <div class="btn btn-white" style="left:632px;top:856px;width:142px;height:48px;font-size:18px">Read More</div>
  </div>
</section>

<div class="abs testi-title">Our Testimonials</div>
<section class="abs testi-band">
  <div class="card side" style="left:-368px">
    <div class="name">Mara Lint</div><div class="year">2022</div><div class="stars">★★★★★</div>
    <div class="quote">Lorem ipsum dolor sit amet, consectetur adipiscing elit, sed do eiusmod tempor incididunt ut labore et dolore magna aliqua. Ut enim ad minim veniam, quis nostrud exercitation ullamco laboris nisi ut aliquip ex ea commodo consequat. Duis aute irure dolor in reprehenderit in voluptate velit esse cillum dolore eu fugiat nulla pariatur</div>
  </div>
  <div class="card" style="left:340px">
    <div class="name">Mara Lint</div><div class="year">2022</div><div class="stars">★★★★★</div>
    <div class="quote"><span class="qmark" style="left:-2px;top:-12px">“</span>Lorem ipsum dolor sit amet, consectetur adipiscing elit, sed do eiusmod tempor incididunt ut labore et dolore magna aliqua. Ut enim ad minim veniam, quis nostrud exercitation ullamco laboris nisi ut aliquip ex ea commodo consequat. Duis aute irure dolor in reprehenderit in voluptate velit esse cillum dolore eu fugiat nulla pariatur<span class="qmark" style="right:40px;bottom:-26px">”</span></div>
  </div>
  <div class="card side" style="left:960px">
    <div class="name">Mara Lint</div><div class="year">2022</div><div class="stars">★★★★★</div>
    <div class="quote">Lorem ipsum dolor sit amet, consectetur adipiscing elit, sed do eiusmod tempor incididunt ut labore et dolore magna aliqua. Ut enim ad minim veniam, quis nostrud exercitation ullamco laboris nisi ut aliquip ex ea commodo consequat. Duis aute irure dolor in reprehenderit in voluptate velit esse cillum dolore eu fugiat nulla pariatur</div>
  </div>
</section>

<section class="abs video-band">
  <div class="section-title" style="top:50px">OUR VIDEO</div>
</section>
<div class="abs video" role="img" aria-label="Illustration of four colleagues relaxing and chatting in lounge chairs">
  <svg class="abs" style="left:454px;top:206px" width="66" height="66" viewBox="0 0 66 66">
    <circle cx="33" cy="33" r="31" fill="#e02020" stroke="#fff" stroke-width="3"/>
    <path d="M26 20v26l21-13z" fill="#fff"/>
  </svg>
</div>

<section class="contact">
  <h2>Get in Touch</h2>
  <p class="lead">Lorem ipsum dolor sit amet, consectetur adipiscing elit, tempor incididunt<br>ut labore et dolore magna aliqua.</p>
  <div class="field" style="top:3613px;height:63px;padding-top:20px">Name</div>
  <div class="field" style="top:3705px;height:63px;padding-top:20px">Email</div>
  <div class="field" style="top:3794px;height:137px">Message</div>

  <div class="icon" style="top:3607px">
    <svg width="22" height="28" viewBox="0 0 22 28"><path d="M11 1a10 10 0 0 0-10 10c0 7 10 16 10 16s10-9 10-16A10 10 0 0 0 11 1z" fill="none" stroke="#fff" stroke-width="2.4"/><circle cx="11" cy="11" r="3.5" fill="#fff"/></svg>
  </div>
  <div class="info" style="top:3615px">Lorem ipsum dolor sit amet, consectetur<br>adipiscing elit</div>

  <div class="icon" style="top:3696px">
    <svg width="26" height="20" viewBox="0 0 26 20"><rect x="1.5" y="1.5" width="23" height="17" rx="2" fill="none" stroke="#fff" stroke-width="2.4"/><path d="M2 3l11 9 11-9" fill="none" stroke="#fff" stroke-width="2.4"/></svg>
  </div>
  <div class="info" style="top:3703px">info@velquo.com<br>hello@velquo.net</div>

  <div class="icon" style="top:3796px">
    <svg width="24" height="24" viewBox="0 0 24 24"><path fill="#fff" d="M6.6 10.8a15.1 15.1 0 0 0 6.6 6.6l2.2-2.2c.3-.3.7-.4 1-.2 1.1.4 2.3.6 3.6.6.6 0 1 .4 1 1V20c0 .6-.4 1-1 1A17 17 0 0 1 3 4c0-.6.4-1 1-1h3.5c.6 0 1 .4 1 1 0 1.3.2 2.5.6 3.6.1.3 0 .7-.2 1z"/></svg>
  </div>
  <div class="info" style="top:3803px">+1 555 014 2290<br>+1 555 014 7731</div>
</section>

<footer class="abs footer">
  <div class="addr">
    <span style="color:var(--orange)">●</span> 58 Sed ut perspiciatis unde omnis iste natus error sit voluptatem accusantium doloremque<br>
    <span style="color:var(--orange)">✆</span> +1 555 014 2290 | <span style="color:var(--orange)">✉</span> info@velquo.com
  </div>
  <div class="logo">Velquo</div>
  <div class="links"><span>Home</span><span>About</span><span>how its work</span><span>Blog</span><span>Contact</span></div>
  <div class="copy">© copyrights 2022 &nbsp;Velquo | &nbsp;All Rights Reserved</div>
</footer>

</body>
</html>
```